Modern Billboard Ad for Criminal Defense Firm

10.5 x 36 We're looking for something to set us apart from the local competition. Looking for sleek and modern. We're a mid-sized firm in a small market city. We want to give the artist room to be creative on this one.
Thanks

Target Market(s)

Adult clients who have been charged with a crime/DWI

Industry/Entity Type

legal

Font styles to use
Serif
Sans Serif

Requirements
Must have
• Needs to have the firm name in large lettering. Law Offices of Marcus T Whitfield. “PLLC” does not have to be included. Phone number of (555) 384-1927 should be included but not the main focus.
Nice to have
• A call to action or something similar. “Don’t go it alone, call today.”, “ Arrested?”

```html
<!DOCTYPE html>
<html lang="en">
<head>
<meta charset="utf-8">
<title>Law Offices of Marcus T Whitfield</title>
<link rel="stylesheet" href="https://fonts.googleapis.com/css2?family=Cinzel:wght@400;500;600&display=swap">
<style>
  :root {
    --navy: #031e33;
    --cream: #d7cdb0;
  }
  html, body {
    margin: 0;
    padding: 0;
    width: 1200px;
    height: 1200px;
    overflow: hidden;
    background: var(--navy);
  }
  .billboard {
    display: block;
    width: 1200px;
    height: 1200px;
    background: var(--navy);
  }
  .billboard text {
    fill: var(--cream);
    font-family: "Cinzel", "Times New Roman", serif;
  }
  .firm-prefix { font-size: 66px; font-weight: 500; }
  .firm-name { font-size: 258px; font-weight: 400; }
  .call-line { font-size: 66px; font-weight: 500; }
  .call-number { font-size: 74px; }
</style>
</head>
<body>
  <svg class="billboard" viewBox="0 0 1200 1200" xmlns="http://www.w3.org/2000/svg" role="img" aria-label="Law Offices of Marcus T Whitfield. Call (555) 384-1927">
    <text class="firm-prefix" x="154" y="377" textLength="564" lengthAdjust="spacingAndGlyphs">LAW OFFICES OF</text>
    <text class="firm-name" x="154" y="591" textLength="886" lengthAdjust="spacingAndGlyphs">MARCUS T</text>
    <text class="firm-name" x="154" y="784" textLength="896" lengthAdjust="spacingAndGlyphs">WHITFIELD</text>
    <text class="call-line" x="154" y="870" textLength="737" lengthAdjust="spacingAndGlyphs">CALL <tspan class="call-number">(555)</tspan> 384-1927</text>
  </svg>
</body>
</html>
```